Revamp Website To A More Modern Up To Date Design Concepts

I am looking for a renewed look for my website.

Keep in mind that my business is B2B.

Please use and include all current content, text and imagery (you can adjust the imagery to fit your designs) and all current modules, features, videos, calls to action buttons, etc. Please do not omit anything from the current homepage. I prefer to see all my content as it is on my current site on the new design too so I can really invision my new site...so please do not use lipsum lorem text filler anywhere.

I am looking for an impressive looking and engaging high converting homepage.

Please be sure to keep all elements, links in header and footer etc. already on my current homepage at www.brightlanepromoworks.biz

Industry/Entity Type

marketing

Coding

Coded - Design and coding required

Number of Pages Required

3 page

Requirements
Must have
• impressive design
Nice to have
• im open
Should not have
• open

```html
<!DOCTYPE html>
<html lang="en">
<head>
<meta charset="utf-8">
<title>Brightlane Promo Works – Homepage Concept</title>
<link href="https://fonts.googleapis.com/css2?family=Montserrat:wght@400;600;700;800;900&family=Open+Sans:wght@400;600&display=swap" rel="stylesheet">
<style>
:root{
  --stage:#eef0f3;
  --page:#ffffff;
  --blue:#1a73c9;
  --blue-dark:#0e4f99;
  --blue-soft:#e6f1fc;
  --ink:#1c2a3d;
  --muted:#8793a3;
  --line:#d9e2ee;
  --orange:#f4a21d;
}
*{box-sizing:border-box;margin:0;padding:0}
html,body{width:755px;height:1200px;overflow:hidden;background:var(--stage)}
body{position:relative;font-family:"Open Sans",Arial,sans-serif;color:var(--ink)}
.page-col{position:absolute;top:12px;width:228px;background:var(--page);overflow:hidden;box-shadow:0 0 6px rgba(0,0,0,.06)}
.col-left{left:146px;height:1178px}
.col-right{left:406px;height:1108px}
h2,h3,.heading{font-family:"Montserrat",Arial,sans-serif}
.section-title{font-family:"Montserrat",Arial,sans-serif;font-weight:800;font-size:6.5px;text-align:center;line-height:1.25;color:var(--ink);text-transform:uppercase}
.section-title em{font-style:normal;color:var(--blue)}
.tiny{font-size:3.2px;line-height:1.5;color:var(--muted)}
.btn{display:block;margin:0 auto;width:52px;height:8px;border-radius:4px;background:var(--blue);color:#fff;font-family:"Montserrat",Arial,sans-serif;font-weight:700;font-size:3.4px;text-align:center;line-height:8px}
.placeholder{display:block}
/* header */
.site-header{height:12px;display:flex;align-items:center;justify-content:space-between;padding:0 8px;border-bottom:1px solid var(--line)}
.brand{display:flex;align-items:center;gap:2px;font-family:"Montserrat",Arial,sans-serif;font-weight:800;font-size:5px;color:var(--blue)}
.brand i{width:5px;height:5px;background:var(--blue);border-radius:50%}
.nav{display:flex;gap:5px;font-size:3px;color:var(--ink)}
/* hero */
.hero{position:relative;height:150px;background:linear-gradient(180deg,#f4f9ff,#dcebfb)}
.hero-copy{position:absolute;left:12px;top:12px;width:105px}
.hero-kicker{font-family:"Montserrat",Arial,sans-serif;font-weight:700;font-size:6px;color:var(--blue-dark)}
.hero-title{font-family:"Montserrat",Arial,sans-serif;font-weight:900;font-size:17px;line-height:.95;color:var(--orange);letter-spacing:-.3px}
.hero-title span{color:var(--blue-dark)}
.hero-sub{font-family:"Montserrat",Arial,sans-serif;font-weight:800;font-size:12px;color:var(--blue-dark)}
.hero-photo{position:absolute;right:10px;top:6px;width:95px;height:104px;border-radius:4px}
.hero-band{position:absolute;left:0;right:0;bottom:0;height:42px;background:var(--blue);display:flex;justify-content:space-around;align-items:center;padding:0 10px}
.stat{display:flex;flex-direction:column;align-items:center;gap:2px;color:#fff;font-size:3px;text-align:center;width:30px}
.stat svg{width:10px;height:10px}
/* areas */
.areas{padding:10px 8px 0}
.areas .section-title{margin-bottom:6px}
.card-row{display:grid;grid-template-columns:repeat(4,1fr);gap:4px}
.area-card{height:62px;border:1px solid var(--line);border-radius:3px;padding:5px 3px;text-align:center}
.area-card svg{width:10px;height:10px;margin-bottom:3px}
.area-card b{display:block;font-family:"Montserrat",Arial,sans-serif;font-size:3.4px;margin-bottom:2px}
.area-card .btn{width:26px;height:5px;line-height:5px;font-size:2.6px;margin-top:4px}
/* incentives list */
.incentives{padding:22px 14px 0}
.incentives .section-title{margin-bottom:8px}
.check-list{list-style:none;display:flex;flex-direction:column;gap:5px;margin-bottom:8px}
.check-list li{display:flex;gap:4px;align-items:flex-start;font-size:3.3px;line-height:1.45;color:var(--muted)}
.check-list svg{flex:none;width:5px;height:5px;margin-top:.5px}
/* media rows */
.media-block{padding:24px 10px 0}
.media-block .section-title{margin-bottom:8px}
.media-row{display:flex;gap:7px;align-items:center}
.media-row .placeholder{flex:none;border-radius:3px}
.media-text{flex:1}
.media-text .btn{margin:5px 0 0;width:40px}
/* bottom cards */
.trio{display:grid;grid-template-columns:repeat(3,1fr);gap:5px;padding:22px 14px 0}
.trio-card{height:72px;border:1px solid var(--line);border-radius:3px;padding:6px 4px;text-align:center;background:#fbfdff}
.trio-card svg{width:11px;height:11px;margin-bottom:3px}
.trio-card b{display:block;font-family:"Montserrat",Arial,sans-serif;font-size:3.4px;margin-bottom:2px}
.left-foot{position:absolute;bottom:0;left:0;right:0;height:130px;padding:40px 20px 0;text-align:center}
/* right column */
.mini-cards{display:grid;grid-template-columns:repeat(3,1fr);gap:5px;padding:6px 14px}
.mini-card{height:30px;border:1px solid var(--line);border-radius:3px;padding:4px;text-align:center}
.mini-card svg{width:8px;height:8px}
.partner-row{display:flex;justify-content:space-around;align-items:center;padding:6px 14px 10px}
.partner-row span{width:26px;height:5px;border-radius:2px;background:#c3ccd8}
.video-band{background:var(--blue);padding:12px 10px;display:grid;grid-template-columns:repeat(3,1fr);gap:5px}
.video-thumb{position:relative;height:38px;border-radius:2px}
.video-thumb p{font-size:3px;color:#fff;margin-top:40px}
.play{position:absolute;left:50%;top:50%;width:9px;height:9px;transform:translate(-50%,-50%)}
.feature-video{padding:30px 18px 0;text-align:center}
.feature-video .section-title{margin-bottom:8px}
.feature-video .frame{position:relative;height:78px;border-radius:3px;margin-bottom:7px}
.illus{margin:22px auto 0;width:110px;height:52px;border-radius:3px}
.clients{margin-top:12px;background:var(--blue-dark);padding:8px 12px 12px;text-align:center}
.clients h3{color:#fff;font-size:5px;font-weight:700;margin-bottom:7px}
.client-logos{display:flex;justify-content:space-between}
.client-logos span{width:30px;height:8px;border-radius:2px;background:rgba(255,255,255,.85)}
.guarantee{position:relative;height:98px;margin-top:16px;padding:0 14px}
.guarantee-badge{position:absolute;left:12px;top:18px;width:60px;font-family:"Montserrat",Arial,sans-serif;font-weight:900;color:var(--blue-dark);line-height:1}
.guarantee-badge b{display:block;font-size:17px;letter-spacing:-.3px}
.guarantee-badge span{display:block;font-size:7.4px;letter-spacing:-.1px}
.guarantee-photo{position:absolute;left:78px;top:4px;width:50px;height:90px;border-radius:3px}
.guarantee-copy{position:absolute;left:134px;top:16px;width:84px}
.guarantee-copy h3{font-size:5.2px;font-weight:800;line-height:1.2;margin-bottom:4px}
.plans{padding:14px 22px 0}
.plans .section-title{margin-bottom:8px}
.plan-row{display:grid;grid-template-columns:1fr 1fr;gap:8px}
.plan{height:212px;border-radius:5px;padding:10px 6px;text-align:center;background:#fff;border:1px solid var(--line)}
.plan.featured{background:var(--blue);color:#fff;border:none}
.plan h4{font-family:"Montserrat",Arial,sans-serif;font-size:4px;font-weight:700}
.price{font-family:"Montserrat",Arial,sans-serif;font-weight:800;font-size:13px;margin:4px 0 6px}
.plan ul{list-style:none;text-align:left;display:flex;flex-direction:column;gap:3.3px;font-size:3px;line-height:1.3}
.plan li::before{content:"✓ ";color:var(--orange)}
.plan .btn{margin-top:8px;background:var(--orange)}
.site-footer{position:absolute;left:0;right:0;bottom:0;height:102px;background:var(--blue-dark);color:#d9e7f7;padding:12px 14px}
.foot-brand{text-align:center;margin-bottom:8px}
.foot-brand .brand{justify-content:center;color:#fff}
.foot-cols{display:grid;grid-template-columns:repeat(4,1fr);gap:6px;font-size:3px;line-height:1.7}
.foot-cols b{display:block;font-family:"Montserrat",Arial,sans-serif;color:#fff;font-size:3.4px}
.foot-bottom{margin-top:8px;border-top:1px solid rgba(255,255,255,.2);padding-top:4px;font-size:3px;text-align:center}
</style>
</head>
<body>

<!-- left half of homepage -->
<main class="page-col col-left">
  <header class="site-header">
    <div class="brand"><i></i>BLP</div>
    <nav class="nav"><span>Home</span><span>About</span><span>Incentives</span><span>Pricing</span><span>Contact</span></nav>
  </header>

  <section class="hero">
    <div class="hero-copy">
      <div class="hero-kicker">POSITIVE</div>
      <div class="hero-title"><span>SALES</span> LEADS</div>
      <div class="hero-sub">Overnight</div>
      <p class="tiny" style="margin-top:6px">Reward prospects with branded incentives that turn interest into real appointments.</p>
    </div>
    <div class="placeholder hero-photo" role="img" aria-label="Smiling businesswoman pointing toward headline" style="background:linear-gradient(160deg,#f6c28b,#e06a3b 55%,#c44a2a)"></div>
    <div class="hero-band">
      <div class="stat"><svg viewBox="0 0 10 10"><circle cx="5" cy="5" r="4" fill="none" stroke="#fff" stroke-width=".8"/><path d="M3 5l1.5 1.5L7 3.5" fill="none" stroke="#fff" stroke-width=".8"/></svg>Proven Results</div>
      <div class="stat"><svg viewBox="0 0 10 10"><rect x="1.5" y="2" width="7" height="6" fill="none" stroke="#fff" stroke-width=".8"/></svg>Branded Gifts</div>
      <div class="stat"><svg viewBox="0 0 10 10"><path d="M1 8h8M2 8V5M5 8V3M8 8V1.5" stroke="#fff" stroke-width=".8"/></svg>More Sales</div>
      <div class="stat"><svg viewBox="0 0 10 10"><circle cx="5" cy="4" r="2" fill="none" stroke="#fff" stroke-width=".8"/><path d="M1.5 9c1-2.5 6-2.5 7 0" fill="none" stroke="#fff" stroke-width=".8"/></svg>Loyal Clients</div>
    </div>
  </section>

  <section class="areas">
    <h2 class="section-title">The 4 Major Areas That<br><em>Matter Most To Your Business</em></h2>
    <div class="card-row">
      <div class="area-card"><svg viewBox="0 0 10 10"><circle cx="5" cy="5" r="4" fill="none" stroke="#1a73c9" stroke-width=".8"/></svg><b>Lead Generation</b><p class="tiny">Attract new qualified buyers fast.</p><span class="btn">Learn More</span></div>
      <div class="area-card"><svg viewBox="0 0 10 10"><rect x="1.5" y="1.5" width="7" height="7" fill="none" stroke="#1a73c9" stroke-width=".8"/></svg><b>Closing Sales</b><p class="tiny">Give buyers a reason to act now.</p><span class="btn">Learn More</span></div>
      <div class="area-card"><svg viewBox="0 0 10 10"><path d="M5 1l4 8H1z" fill="none" stroke="#1a73c9" stroke-width=".8"/></svg><b>Client Loyalty</b><p class="tiny">Keep customers coming back.</p><span class="btn">Learn More</span></div>
      <div class="area-card"><svg viewBox="0 0 10 10"><path d="M1 8h8M2 8V5M5 8V3M8 8V1.5" stroke="#1a73c9" stroke-width=".8"/></svg><b>Referrals</b><p class="tiny">Reward clients who send friends.</p><span class="btn">Learn More</span></div>
    </div>
  </section>

  <section class="incentives">
    <h2 class="section-title">Distribute Valued Priced Incentives<br><em>Branded With Your Logo...</em></h2>
    <ul class="check-list">
      <li><svg viewBox="0 0 5 5"><circle cx="2.5" cy="2.5" r="2.5" fill="#1a73c9"/><path d="M1.3 2.6l.9.8 1.6-1.7" fill="none" stroke="#fff" stroke-width=".5"/></svg>Vacation and hotel certificates your clients will actually use and remember.</li>
      <li><svg viewBox="0 0 5 5"><circle cx="2.5" cy="2.5" r="2.5" fill="#1a73c9"/><path d="M1.3 2.6l.9.8 1.6-1.7" fill="none" stroke="#fff" stroke-width=".5"/></svg>Dining, shopping and entertainment rewards with high perceived value.</li>
      <li><svg viewBox="0 0 5 5"><circle cx="2.5" cy="2.5" r="2.5" fill="#1a73c9"/><path d="M1.3 2.6l.9.8 1.6-1.7" fill="none" stroke="#fff" stroke-width=".5"/></svg>Every incentive carries your company logo and contact details.</li>
      <li><svg viewBox="0 0 5 5"><circle cx="2.5" cy="2.5" r="2.5" fill="#1a73c9"/><path d="M1.3 2.6l.9.8 1.6-1.7" fill="none" stroke="#fff" stroke-width=".5"/></svg>Instant online delivery by email, text or printed card.</li>
      <li><svg viewBox="0 0 5 5"><circle cx="2.5" cy="2.5" r="2.5" fill="#1a73c9"/><path d="M1.3 2.6l.9.8 1.6-1.7" fill="none" stroke="#fff" stroke-width=".5"/></svg>Track redemptions and follow up with warm leads daily.</li>
      <li><svg viewBox="0 0 5 5"><circle cx="2.5" cy="2.5" r="2.5" fill="#1a73c9"/><path d="M1.3 2.6l.9.8 1.6-1.7" fill="none" stroke="#fff" stroke-width=".5"/></svg>Low fixed cost with unlimited distribution each month.</li>
    </ul>
    <span class="btn">Get Started Today</span>
  </section>

  <section class="media-block">
    <h2 class="section-title">Watch Video Of BLP's<br><em>Automation Features In Action</em></h2>
    <div class="media-row">
      <div class="placeholder" role="img" aria-label="Video still of presenter in office" style="width:104px;height:66px;background:linear-gradient(135deg,#3b4a5e,#9aa9bb)"></div>
      <div class="media-text"><p class="tiny">See how our platform sends, tracks and follows up on every incentive automatically so your team can focus on closing.</p><span class="btn">Watch Now</span></div>
    </div>
  </section>

  <section class="media-block">
    <h2 class="section-title">Giveaway Unlimited Incentives<br><em>That Range In Retail Value Of $25-$1000</em></h2>
    <div class="media-row">
      <div class="placeholder" role="img" aria-label="Two laptops showing incentive catalog screens" style="width:104px;height:82px;background:linear-gradient(135deg,#f2a33c,#7a3db8 60%,#2b2f3a)"></div>
      <div class="media-text"><p class="tiny">Choose from hundreds of travel, dining and lifestyle offers. Give as many as you like to prospects, clients and staff.</p><span class="btn">View Catalog</span></div>
    </div>
  </section>

  <section class="media-block">
    <div class="media-row">
      <h2 class="section-title" style="text-align:left;width:100px">Done For You Promotional<br><em>Marketing, White Label &amp; More</em></h2>
      <div class="media-text"><p class="tiny">Our team builds your campaign, brands every piece and launches it for you.</p><span class="btn">Learn More</span></div>
    </div>
  </section>

  <section class="trio">
    <div class="trio-card"><svg viewBox="0 0 11 11"><rect x="1" y="2" width="9" height="7" rx="1" fill="none" stroke="#1a73c9" stroke-width=".8"/></svg><b>White Label</b><p class="tiny">Your brand on every offer.</p></div>
    <div class="trio-card"><svg viewBox="0 0 11 11"><circle cx="5.5" cy="5.5" r="4" fill="none" stroke="#1a73c9" stroke-width=".8"/></svg><b>Full Service</b><p class="tiny">We run the whole campaign.</p></div>
    <div class="trio-card"><svg viewBox="0 0 11 11"><path d="M1.5 9h8M3 9V6M5.5 9V3.5M8 9V2" stroke="#1a73c9" stroke-width=".8"/></svg><b>Reporting</b><p class="tiny">Clear results every week.</p></div>
  </section>

  <div class="left-foot"><p class="tiny">Questions? Our team is ready to help you plan your first campaign.</p></div>
</main>

<!-- right half of homepage -->
<main class="page-col col-right">
  <div class="mini-cards">
    <div class="mini-card"><svg viewBox="0 0 8 8"><circle cx="4" cy="4" r="3" fill="none" stroke="#1a73c9" stroke-width=".7"/></svg><p class="tiny">Easy setup</p></div>
    <div class="mini-card"><svg viewBox="0 0 8 8"><rect x="1" y="1" width="6" height="6" fill="none" stroke="#1a73c9" stroke-width=".7"/></svg><p class="tiny">Fast delivery</p></div>
    <div class="mini-card"><svg viewBox="0 0 8 8"><path d="M4 1l3 6H1z" fill="none" stroke="#1a73c9" stroke-width=".7"/></svg><p class="tiny">Real savings</p></div>
  </div>
  <div class="partner-row"><span></span><span></span><span></span><span></span><span></span></div>

  <section class="video-band">
    <div class="video-thumb placeholder" role="img" aria-label="Client testimonial video still" style="background:linear-gradient(135deg,#44546a,#a4b3c4)"><svg class="play" viewBox="0 0 9 9"><circle cx="4.5" cy="4.5" r="4.5" fill="#fff"/><path d="M3.5 2.7v3.6l3-1.8z" fill="#1a73c9"/></svg><p>Client story</p></div>
    <div class="video-thumb placeholder" role="img" aria-label="Client testimonial video still" style="background:linear-gradient(135deg,#5a4a3e,#b9a48e)"><svg class="play" viewBox="0 0 9 9"><circle cx="4.5" cy="4.5" r="4.5" fill="#fff"/><path d="M3.5 2.7v3.6l3-1.8z" fill="#1a73c9"/></svg><p>Client story</p></div>
    <div class="video-thumb placeholder" role="img" aria-label="Client testimonial video still" style="background:linear-gradient(135deg,#3e4f5a,#8ea8b9)"><svg class="play" viewBox="0 0 9 9"><circle cx="4.5" cy="4.5" r="4.5" fill="#fff"/><path d="M3.5 2.7v3.6l3-1.8z" fill="#1a73c9"/></svg><p>Client story</p></div>
  </section>

  <section class="feature-video">
    <h2 class="section-title">Sounds Too Good<br><em>To Be True?</em></h2>
    <div class="frame placeholder" role="img" aria-label="Video still of company founder explaining the program" style="background:linear-gradient(135deg,#2f3b4b,#8d9cad)"><svg class="play" viewBox="0 0 9 9" style="width:12px;height:12px"><circle cx="4.5" cy="4.5" r="4.5" fill="#fff"/><path d="M3.5 2.7v3.6l3-1.8z" fill="#1a73c9"/></svg></div>
    <p class="tiny">Hear directly from our founder how businesses use our incentives to open doors, win meetings and close more deals without raising their marketing budget.</p>
  </section>

  <div class="illus placeholder" role="img" aria-label="Illustration of two office buildings" style="background:linear-gradient(180deg,#e6f1fc,#b9d6f3)"></div>

  <section class="clients">
    <h3 class="heading">Our Clients</h3>
    <div class="client-logos"><span></span><span></span><span></span><span></span><span></span></div>
  </section>

  <section class="guarantee">
    <div class="guarantee-badge"><b>100%</b><span>GUARANTEE</span></div>
    <div class="guarantee-photo placeholder" role="img" aria-label="Smiling woman giving thumbs up" style="background:linear-gradient(180deg,#f5c98f,#f0a93a)"></div>
    <div class="guarantee-copy"><h3 class="heading">Risk Free Trial<br>15-Day Money Back Guarantee</h3><p class="tiny">Try the full program. If it is not right for you, get a complete refund.</p></div>
  </section>

  <section class="plans">
    <h2 class="section-title">Choose Your Plan</h2>
    <div class="plan-row">
      <div class="plan featured">
        <h4>Monthly Plan</h4>
        <div class="price">$99</div>
        <ul><li>Unlimited incentives</li><li>Your logo on every offer</li><li>Email and text delivery</li><li>Lead tracking dashboard</li><li>Printable certificates</li><li>Phone and email support</li><li>Cancel anytime</li><li>Setup included</li></ul>
        <span class="btn">Sign Up</span>
      </div>
      <div class="plan">
        <h4>Annual Plan</h4>
        <div class="price" style="color:var(--blue-dark)">$898</div>
        <ul style="color:var(--muted)"><li>Unlimited incentives</li><li>Your logo on every offer</li><li>Email and text delivery</li><li>Lead tracking dashboard</li><li>Printable certificates</li><li>Priority support</li><li>Two months free</li><li>Setup included</li></ul>
        <span class="btn">Sign Up</span>
      </div>
    </div>
  </section>

  <footer class="site-footer">
    <div class="foot-brand"><div class="brand"><i style="background:#fff"></i>BLP</div></div>
    <div class="foot-cols">
      <div><b>Company</b>About<br>Careers<br>Contact</div>
      <div><b>Programs</b>Incentives<br>White Label<br>Pricing</div>
      <div><b>Support</b>FAQ<br>Help Desk<br>Terms</div>
      <div><b>Visit</b>www.brightlanepromoworks.biz</div>
    </div>
    <div class="foot-bottom">© Brightlane Promo Works. All rights reserved.</div>
  </footer>
</main>

</body>
</html>
```